Process Roadmap for Interior Design Firm

We are looking to ramp up the design appeal of our current process roadmap to be very visually interesting, while staying informative and descriptive about our process.

Target Market(s)

In-house Clients

Industry/Entity Type

Interior Design Firm focused on sustainable and holistic design.

Other font styles liked:
• raleway

Requirements
Must have
• 1.) it would be nice if the graphic provided a more clear indication of the “journey” from one step to the next, so that there was a clear sense of the progression (such that we are directing the viewer) 2.). We would want it to fit on an 8.5”x11” page (the page could be horizontal when we have the Calm Compass formatted out with the testimonials) (in addition to the testimonials, we may also want to have the detailed descriptions of each step of the process presented below the graphic, so that the graphic is cleaner) 3.) ideally the graphic is clear and simple enough to also be used on our Bi-Weekly Client Updates, which will be typed updates for clients re their project budgets, schedule and scope. The Calm Compass graphic (without all the testimonials) would be at the end of the update, and would fit on the page horizontally at the bottom, perhaps in a space which is 7.5”w x 4”h or so.
Should not have
• bold or bright colors. Natural neutrals are preferred, such as the ones featured on the provided graphic.

```html
<!DOCTYPE html>
<html lang="en">
<head>
<meta charset="utf-8">
<title>HRD Calm Compass</title>
<link href="https://fonts.googleapis.com/css2?family=Barlow:wght@400;600;700&display=swap" rel="stylesheet">
<style>
  :root {
    --paper: #f7f6f4;
    --white: #ffffff;
    --sand: #c4b49a;
    --sand-light: #dcd2c2;
    --ink: #b1a386;
    --heading: #b5a68a;
  }
  * { margin: 0; padding: 0; box-sizing: border-box; }
  html, body { width: 1200px; height: 927px; overflow: hidden; }
  body {
    font-family: "Barlow", Arial, sans-serif;
    background: var(--white);
    color: var(--ink);
    position: relative;
  }
  .roadmap-area {
    position: absolute; left: 0; top: 0; width: 1200px; height: 691px;
    background: var(--paper);
  }
  .brand {
    position: absolute; left: 53px; top: 52px; height: 58px;
    display: flex; align-items: center; gap: 10px;
  }
  .brand-square { width: 14px; height: 14px; background: var(--sand); }
  .brand-name { font-size: 17px; font-weight: 600; color: var(--sand); letter-spacing: 0.5px; }
  .title-band {
    position: absolute; left: 756px; top: 52px; width: 393px; height: 58px;
    background: var(--sand); color: var(--white);
    font-size: 25px; font-weight: 700;
    display: flex; align-items: center; justify-content: center;
  }
  .wave { position: absolute; left: 0; top: 0; }
  .step-card {
    position: absolute; width: 215px;
    background: linear-gradient(90deg, rgba(255,255,255,0.95) 35%, rgba(255,255,255,0));
    padding: 0 0 0 13px;
  }
  .step-card p { font-size: 15.5px; line-height: 18.2px; }
  .step-card p + p { margin-top: 18px; }
  .step-card h2 { font-size: 19px; font-weight: 700; color: var(--heading); line-height: 22px; }
  .step-card.upper { top: 186px; height: 159px; padding-top: 11px; }
  .step-card.upper h2 { position: absolute; left: 13px; top: 127px; }
  .step-card.lower { top: 419px; height: 181px; padding-top: 12px; }
  .step-card.lower h2 { margin-bottom: 9px; }
  .step-card.lower p.tight + p.tight { margin-top: 9px; }
  .testimonials-label {
    position: absolute; left: 517px; top: 674px; width: 166px; height: 34px;
    background: var(--sand); color: var(--white);
    font-size: 19px; font-weight: 700;
    display: flex; align-items: center; justify-content: center;
  }
  .testimonial {
    position: absolute; top: 762px; width: 180px;
    text-align: center; font-size: 16.5px; line-height: 20.5px; color: var(--ink);
  }
  .testimonial-divider {
    position: absolute; top: 786px; height: 73px; width: 0;
    border-left: 2px dashed var(--sand-light);
  }
</style>
</head>
<body>
  <section class="roadmap-area">
    <div class="brand">
      <span class="brand-square"></span>
      <span class="brand-name">Hollis Reed Design</span>
    </div>
    <div class="title-band">HRD Calm Compass</div>

    <div class="step-card upper" style="left:202px">
      <p>Facilitating a guided visioning process to clarify the deepest intention, true purpose, and highest potential for their home and their future within it.</p>
      <h2>Visioning</h2>
    </div>
    <div class="step-card upper" style="left:499px; width:230px">
      <p>Following the schedule through the design phases from initial design concepts, technical drawings and details, and the selection of all finishes, fixtures, and surnishings.</p>
      <h2>Designing</h2>
    </div>
    <div class="step-card upper" style="left:796px; width:230px">
      <p>Overseeing the inspection, installation, and arrangement of all furnishings, lighting, artwork, and decorative items.</p>
      <p>Taking care of every last detail.</p>
      <h2>Installing</h2>
    </div>

    <div class="step-card lower" style="left:54px; width:210px">
      <h2>Listening</h2>
      <p>Listening to our clients, their land, and their home.</p>
      <p>Identifying their needs, challenges, wishes, and dreams.</p>
    </div>
    <div class="step-card lower" style="left:351px; width:215px">
      <h2>Planning</h2>
      <p>Turning our client's vision into a clearly defined scope., budget, and timeline. Mapping out the steps for making their dream a reality. Setting a meeting schedule from start to finish.</p>
    </div>
    <div class="step-card lower" style="left:648px; width:225px">
      <h2>Managing</h2>
      <p>Coordinating with clients, builders, architects, and vendors to ensure that the design is executed with excellence, and the construction and furnishings are on-time and on-budget.</p>
    </div>
    <div class="step-card lower" style="left:948px; width:210px; padding-left:10px">
      <h2>Completing</h2>
      <p class="tight">Fixing any issues or defects.</p>
      <p class="tight">Follow up on all remaining items.</p>
      <p class="tight">Completing the final finishing touches to our client's full and total satisfaction.</p>
    </div>

    <svg class="wave" width="1200" height="691" viewBox="0 0 1200 691" aria-hidden="true">
      <g stroke="var(--sand-light)" stroke-width="1.6" stroke-dasharray="4 4">
        <line x1="106" y1="372" x2="106" y2="430"/>
        <line x1="254" y1="333" x2="254" y2="389"/>
        <line x1="403" y1="372" x2="403" y2="430"/>
        <line x1="552" y1="333" x2="552" y2="389"/>
        <line x1="700" y1="372" x2="700" y2="430"/>
        <line x1="848" y1="333" x2="848" y2="389"/>
        <line x1="997" y1="372" x2="997" y2="430"/>
      </g>
      <path d="M51,351 L106,350 C180,350 180,411 254,411 C328,411 328,350 403,350 C477,350 477,411 552,411 C626,411 626,350 700,350 C774,350 774,411 848,411 C922,411 922,350 997,350 L1150,351"
            fill="none" stroke="var(--sand)" stroke-width="2.6"/>
      <g fill="var(--white)" stroke="var(--sand)" stroke-width="2.6">
        <circle cx="106" cy="350" r="22"/>
        <circle cx="254" cy="411" r="22"/>
        <circle cx="403" cy="350" r="22"/>
        <circle cx="552" cy="411" r="22"/>
        <circle cx="700" cy="350" r="22"/>
        <circle cx="848" cy="411" r="22"/>
        <circle cx="997" cy="350" r="22"/>
      </g>
      <g fill="var(--sand)" font-family="Barlow, Arial, sans-serif" font-size="22" font-weight="700" text-anchor="middle">
        <text x="106" y="358">1</text>
        <text x="254" y="419">2</text>
        <text x="403" y="358">3</text>
        <text x="552" y="419">4</text>
        <text x="700" y="358">5</text>
        <text x="848" y="419">6</text>
        <text x="997" y="358">7</text>
      </g>
    </svg>
  </section>

  <div class="testimonials-label">Testimonials</div>

  <p class="testimonial" style="left:90px">Hollis to send over testimonials for fill this space - three or four columns of testimonials</p>
  <span class="testimonial-divider" style="left:319px"></span>
  <p class="testimonial" style="left:369px">Hollis to send over testimonials for fill this space - three or four columns of testimonials</p>
  <span class="testimonial-divider" style="left:600px"></span>
  <p class="testimonial" style="left:650px">Hollis to send over testimonials for fill this space - three or four columns of testimonials</p>
  <span class="testimonial-divider" style="left:880px"></span>
  <p class="testimonial" style="left:929px">Hollis to send over testimonials for fill this space - three or four columns of testimonials</p>
</body>
</html>
```